We need a website design for an HVAC (Heating & Air Conditioning) Contractor*

Our HVAC client would like to have a more professional looking site as their current one (https://brindlecoolingworks.example/) is a template site. We will be building the site in-house from the concept.
Items we'd like to incorporate:
- A banner on the homepage that has a click to call plus a form on the right side of the banner
- There is a video on the current website homepage, please find a place to incorporate this.
- We will need to have at least 800 words of content on the homepage, please find space for that (can be a description of a few of the heating / air conditioning services they do). Feel free to use filler content (lorem ipsum) if need be to just show how the content would look

All submissions must have a homepage and a related subpage concept.

```html
<!DOCTYPE html>
<html lang="en">
<head>
<meta charset="utf-8">
<title>Brindle Cooling Works – Heating &amp; Air Conditioning</title>
<link href="https://fonts.googleapis.com/css2?family=Oswald:wght@400;500;600&family=Questrial&display=swap" rel="stylesheet">
<style>
:root{
  --red:#c0281c;
  --navy:#1c355e;
  --dark:#1f1f1f;
  --ink:#333;
  --muted:#666;
  --line:#e3e3e3;
  --white:#fff;
}
*{box-sizing:border-box;margin:0;padding:0}
html,body{width:1200px;height:5124px;overflow:hidden}
body{font-family:"Questrial",Arial,sans-serif;color:var(--ink);background:#fff;position:relative}
.abs{position:absolute}
.head{font-family:"Oswald","Arial Narrow",sans-serif;font-weight:500;text-transform:uppercase}
a{color:inherit}

/* top bar */
.topbar{left:0;top:0;width:1200px;height:46px;background:var(--red);color:#fff;font-size:12px;line-height:18px}
.topbar .note{left:90px;top:4px;width:680px}
.topbar .call{left:1002px;top:4px}

/* nav */
.nav{left:0;top:46px;width:1200px;height:78px;background:#fff}
.logo{left:90px;top:58px;font-family:"Oswald",sans-serif;font-weight:600;font-size:26px;color:var(--red);letter-spacing:1px;display:flex;align-items:center;gap:8px}
.logo i{display:block;width:14px;height:14px;background:var(--red)}
.menu{left:278px;top:76px;display:flex;gap:24px;font-size:13px;color:#222}
.menu .on{color:var(--red)}

/* hero */
.hero-photo{left:0;top:124px;width:1200px;height:580px;background:linear-gradient(100deg,#eaeaea 0%,#d8d8d4 35%,#e0d66a 50%,#e7e4de 70%,#f3f3f3 100%)}
.quote{left:653px;top:124px;width:458px;height:580px;background:var(--navy);color:#fff;text-align:center}
.quote h2{font-size:31px;margin-top:52px;font-weight:500}
.quote p{font-size:13px;line-height:20px;width:370px;margin:6px auto 0}
.field{position:absolute;left:38px;width:382px;height:40px;background:#fff;color:#999;font-size:11px;text-align:left;padding:13px 14px;letter-spacing:1px}
.btn-red{background:var(--red);color:#fff;font-family:"Oswald",sans-serif;letter-spacing:1px;text-align:center}

/* about */
.about-photo{left:90px;top:704px;width:471px;height:685px;background:linear-gradient(180deg,#b9b9b7,#d8d8d6 60%,#c4c4c2)}
.about{left:653px;top:790px;width:402px}
.about h2{font-size:35px;color:#111}
.about h3{font-family:"Oswald",sans-serif;font-weight:400;font-size:20px;color:#555;margin-top:10px}
.about .lead{font-size:13px;color:#555;line-height:20px;margin-top:6px}
.about p{font-size:13px;line-height:25px;text-align:justify;margin-top:18px;color:#444}

/* video */
.video{left:0;top:1389px;width:1200px;height:601px;background:linear-gradient(120deg,#6f6b68,#a29a93 40%,#5d6b76 75%,#2a3a52)}
.play{left:554px;top:1645px}

/* services */
.title-center{left:0;width:1200px;text-align:center;color:#111}
.card{top:2137px;width:249px;height:299px;color:#fff}
.card span{position:absolute;left:16px;bottom:16px;font-family:"Oswald",sans-serif;font-weight:500;font-size:21px;line-height:22px;text-transform:uppercase}

/* why us */
.why{left:0;top:2531px;width:603px;height:544px;background:var(--red);color:#fff;padding:92px 0 0 90px}
.why h2{font-size:35px}
.why p{font-size:13px;line-height:22px;width:400px;margin-top:14px}
.why h4{font-family:"Oswald",sans-serif;font-weight:500;font-size:15px;margin-top:20px}
.why ul{list-style:none;font-size:13px;margin-top:14px}
.why li{line-height:24px;padding-left:24px;position:relative}
.why li:before{content:"»";position:absolute;left:0}
.why-photo{left:603px;top:2531px;width:597px;height:544px;background:linear-gradient(180deg,#e9eaec,#cfd2d6 60%,#8a8f96)}

/* cta */
.box{top:3341px;height:313px;color:#fff;text-align:center}
.box .ring{width:88px;height:88px;border:2px solid #fff;border-radius:50%;margin:56px auto 0;display:flex;align-items:center;justify-content:center}
.box h5{font-weight:400;font-size:19px;line-height:28px;margin-top:30px}
.box a{display:block;font-size:12px;margin-top:16px;text-decoration:underline}

/* map */
.map{left:0;top:3749px;width:1200px;height:549px;background:linear-gradient(135deg,#eef0f2,#e2e5e9 50%,#eef0f2)}

/* contact row */
.contact{top:4378px;display:flex;gap:14px;align-items:center}
.contact .dot{width:52px;height:52px;border-radius:50%;background:var(--red);display:flex;align-items:center;justify-content:center}
.contact small{display:block;font-size:12px;color:#777}
.contact b{font-weight:400;font-size:16px;color:#222;line-height:20px}
.badge{top:4517px;height:78px;background:#d9d9d9}

/* footer */
.footer{left:0;top:4633px;width:1200px;height:491px;background:var(--dark);color:#fff}
.footer h6{font-family:"Oswald",sans-serif;font-weight:500;font-size:20px;text-transform:uppercase}
.flinks{left:408px;top:4706px}
.flinks h6,.news h6{font-family:"Oswald",sans-serif;font-weight:500;font-size:20px;text-transform:uppercase}
.flinks ul{list-style:none;font-size:13px;margin-top:22px;line-height:27px}
.news{left:677px;top:4706px;width:432px}
.news p{font-size:13px;line-height:26px;margin-top:22px}
.copy{left:0;top:5088px;width:1200px;text-align:center;font-size:12px;color:#ddd}
</style>
</head>
<body>

<div class="abs topbar">
  <div class="abs note">We Are Open For Business And Ready For Work.Brindle Cooling Works Is An Essential Business And We Take Every Step Necessary When It Comes To Customer Health And Safety</div>
  <div class="abs call">
    <svg width="11" height="11" viewBox="0 0 24 24" fill="#fff"><path d="M6.6 10.8c1.4 2.8 3.8 5.1 6.6 6.6l2.2-2.2c.3-.3.7-.4 1-.2 1.1.4 2.3.6 3.6.6.6 0 1 .4 1 1V20c0 .6-.4 1-1 1C10.6 21 3 13.4 3 4c0-.6.4-1 1-1h3.5c.6 0 1 .4 1 1 0 1.3.2 2.5.6 3.6.1.3 0 .7-.2 1L6.6 10.8z"/></svg>
    &nbsp;Call Us<br>(555) 014-2290</div>
</div>

<div class="abs nav"></div>
<div class="abs logo"><i></i>BRINDLE</div>
<nav class="abs menu">
  <span class="on">Home</span><span>Residential &amp; Commercial Services</span><span>Geothermal</span><span>Contact Us</span><span>Maintenance Plan</span><span>Specials</span><span>Comfort Financing</span>
</nav>

<div class="abs hero-photo" role="img" aria-label="Happy couple on a yellow sofa under a wall-mounted air conditioner"></div>
<section class="abs quote">
  <h2 class="head">Get A Free Quote</h2>
  <p>Lorem ipsum dolor sit amet, consectetur adipiscing elit, sed do eiusmod tempor incididunt ut labore</p>
  <div class="field" style="top:154px">FIRST NAME</div>
  <div class="field" style="top:200px">LAST NAME</div>
  <div class="field" style="top:247px">EMAIL</div>
  <div class="field" style="top:294px">PHONE NUMBER</div>
  <div class="field" style="top:340px;height:136px">MESSAGE</div>
  <div class="btn-red abs" style="left:38px;top:477px;width:382px;height:42px;line-height:42px;font-size:14px">GET A QUOTE</div>
</section>

<div class="abs about-photo" role="img" aria-label="Outdoor air conditioning condenser unit against a white brick wall"></div>
<section class="abs about">
  <h2 class="head">About Us</h2>
  <h3>GO THE ENERGY-EFFICIENT ROUTE</h3>
  <div class="lead">Make Sure You Hire An Experienced Hvac<br>Company In Redfield &amp; Cedar Ridge, Ok</div>
  <p>Brindle Cooling Works, LLC provides a wide variety of residential and commercial HVAC services in the Redfield, OK area. With over a decade of experience, you can trust our HVAC company to install, repair and maintain the HVAC systems in your home or commercial building. Our technician can find out what's wrong with your malfunctioning heating or cooling system and repair or replace it on the spot. We specialize in energy-efficient geothermal heating and cooling systems.</p>
  <p>Call 555-014-2290 now to schedule geothermal system installation or central AC repair services. Find out how a geothermal system can improve your comfort level and reduce your energy bills.</p>
</section>

<div class="abs video" role="img" aria-label="Company video still: family relaxing at home beside a service van"></div>
<svg class="abs play" width="92" height="92" viewBox="0 0 92 92"><circle cx="46" cy="46" r="43" fill="rgba(0,0,0,.15)" stroke="#fff" stroke-width="4"/><path d="M36 28 L66 46 L36 64Z" fill="#fff"/></svg>

<h2 class="abs head title-center" style="top:2080px;font-size:35px">What We Do</h2>
<div class="abs card" style="left:90px;background:linear-gradient(180deg,#6d8fb8,#aab6c0 50%,#6f6a4e)" role="img" aria-label="Geothermal steam field"><span>Geothermal</span></div>
<div class="abs card" style="left:346px;background:linear-gradient(180deg,#b8b4a6,#9ea095 60%,#5d6a4a)" role="img" aria-label="Residential condenser units"><span>Residential HVAC<br>Installation and<br>Repair</span></div>
<div class="abs card" style="left:605px;background:linear-gradient(180deg,#5b6a62,#3f4a48 60%,#2e3636)" role="img" aria-label="Commercial HVAC units"><span>Commercial HVAC<br>Installation and<br>Repair</span></div>
<div class="abs card" style="left:862px;background:linear-gradient(180deg,#b2a89c,#8b6a58 60%,#4c4440)" role="img" aria-label="Technician checking gauges"><span>Maintenance Plan</span></div>

<section class="abs why">
  <h2 class="head">Why Us</h2>
  <p>Your search for a timely, professional HVAC company ends here. Brindle Cooling Works offers HVAC installation and repair services in and around Redfield &amp; Cedar Ridge, OK.</p>
  <h4>CUSTOMERS APPRECIATE OUR HVAC SERVICES BECAUSE</h4>
  <ul>
    <li>We have over 10 years of heating and cooling experience</li>
    <li>We offer free HVAC replacement estimates</li>
    <li>We provide residential and commercial HVAC services</li>
    <li>We offer HVAC maintenance plans</li>
  </ul>
  <p>Contact us today to sign up for an HVAC maintenance plan. We can service your unit routinely to keep your HVAC system up and running.</p>
</section>
<div class="abs why-photo" role="img" aria-label="Technician servicing a ceiling air conditioning vent"></div>

<h2 class="abs head title-center" style="top:3160px;font-size:35px">Tired Of High Energy Bills?</h2>
<div class="abs title-center" style="top:3220px;font-size:19px;color:#333">Turn To Brindle Cooling Works For Geothermal System Installation Services</div>
<div class="abs head" style="left:525px;top:3268px;width:150px;height:42px;line-height:42px;background:var(--navy);color:#fff;text-align:center;font-size:14px;letter-spacing:1px">Learn More</div>

<div class="abs box" style="left:231px;width:364px;background:var(--navy)">
  <div class="ring"><svg width="20" height="20" viewBox="0 0 24 24" fill="#fff"><path d="M7 2v2H5a2 2 0 0 0-2 2v14a2 2 0 0 0 2 2h14a2 2 0 0 0 2-2V6a2 2 0 0 0-2-2h-2V2h-2v2H9V2zM5 9h14v11H5z"/></svg></div>
  <h5>Schedule Your Appointment<br>Today</h5><a>Click Here</a>
</div>
<div class="abs box" style="left:607px;width:362px;background:var(--red)">
  <div class="ring"><svg width="18" height="18" viewBox="0 0 24 24" fill="#fff"><path d="M6.6 10.8c1.4 2.8 3.8 5.1 6.6 6.6l2.2-2.2c.3-.3.7-.4 1-.2 1.1.4 2.3.6 3.6.6.6 0 1 .4 1 1V20c0 .6-.4 1-1 1C10.6 21 3 13.4 3 4c0-.6.4-1 1-1h3.5c.6 0 1 .4 1 1 0 1.3.2 2.5.6 3.6.1.3 0 .7-.2 1L6.6 10.8z"/></svg></div>
  <h5>Contact For Emergency<br>Services</h5><a>Click Here</a>
</div>

<div class="abs map" role="img" aria-label="Street map showing the company location in Redfield"></div>

<div class="abs contact" style="left:90px">
  <div class="dot"><svg width="18" height="18" viewBox="0 0 24 24" fill="#fff"><path d="M6.6 10.8c1.4 2.8 3.8 5.1 6.6 6.6l2.2-2.2c.3-.3.7-.4 1-.2 1.1.4 2.3.6 3.6.6.6 0 1 .4 1 1V20c0 .6-.4 1-1 1C10.6 21 3 13.4 3 4c0-.6.4-1 1-1h3.5c.6 0 1 .4 1 1 0 1.3.2 2.5.6 3.6.1.3 0 .7-.2 1L6.6 10.8z"/></svg></div>
  <div><small>Call Us Today</small><b>(555) 014-2290</b></div>
</div>
<div class="abs contact" style="left:334px">
  <div class="dot"><svg width="14" height="14" viewBox="0 0 14 14"><circle cx="7" cy="7" r="5" fill="#fff"/></svg></div>
  <div><small>Follow Us</small><b>Social Page</b></div>
</div>
<div class="abs contact" style="left:550px">
  <div class="dot"><svg width="20" height="16" viewBox="0 0 20 16"><rect x="1" y="1" width="18" height="14" rx="2" fill="#fff"/><path d="M2 3l8 6 8-6" stroke="var(--red)" stroke-width="2" fill="none"/></svg></div>
  <div><small>Email Us</small><b>hello@brindlecooling.example</b></div>
</div>
<div class="abs contact" style="left:840px">
  <div class="dot"><svg width="22" height="22" viewBox="0 0 22 22"><circle cx="11" cy="11" r="9" fill="none" stroke="#fff" stroke-width="2"/><path d="M11 6v5h4" stroke="#fff" stroke-width="2" fill="none"/></svg></div>
  <div><small>Opening Hours</small><b>Mon - Fri&nbsp; 7:00AM-9:00PM<br>Sat &amp; Sun 8:00AM-5:00PM</b></div>
</div>

<div class="abs" style="left:90px;top:4486px;width:1020px;height:1px;background:var(--line)"></div>
<div class="abs badge" style="left:220px;width:66px;border-radius:6px"></div>
<div class="abs badge" style="left:402px;width:78px;border-radius:50%"></div>
<div class="abs badge" style="left:592px;width:72px;border-radius:6px"></div>
<div class="abs badge" style="left:776px;width:206px;height:56px;top:4528px;border-radius:4px;background:#1f4f8a"></div>

<footer class="abs footer"></footer>
<div class="abs logo" style="top:4740px;color:#fff;font-size:30px"><i style="background:#fff"></i>BRINDLE</div>
<div class="abs" style="left:92px;top:4826px;width:160px;height:48px;background:#4a7fd0;border-radius:4px;color:#fff;font-size:11px;line-height:14px;padding:10px 12px">Click here to leave us<br>a review online</div>
<div class="abs flinks" style="color:#fff">
  <h6>Links</h6>
  <ul><li>Home</li><li>Residential &amp; Commercial</li><li>Services</li><li>Geothermal</li><li>Contact Us</li><li>Maintenance Plan</li><li>Specials</li><li>Comfort Financing</li></ul>
</div>
<div class="abs news" style="color:#fff">
  <h6>Newsletter</h6>
  <p>Lorem ipsum dolor sit amet, consectetur adipiscing elit, sed do eiusmod tempor incididunt ut labore et dolore</p>
  <div style="margin-top:14px;height:40px;background:#fff;color:#888;font-size:13px;padding:12px 18px">Enter Your Email Address</div>
  <div class="btn-red" style="margin-top:6px;height:42px;line-height:42px;font-size:15px">SUBSCRIBE NOW</div>
</div>
<div class="abs copy">© 2021 Copyrights.The Company Name.All Rights Reserved</div>

</body>
</html>
```